Business card design needed

Velvet Twirl-Pop is an online boutique for connoisseurs of unique, hand crafted, vintage and pin-up inspired lingerie, delectable handmade lotions & potions and naughty & nice, seduce me please gifts and ideas.

Inspired by vintage glamour, pin-up and burlesque, the site is dedicated to things that make all women look and feel beautiful…with a touch of mischief.

The design should be clean, uncomplicated, sophisticated and in line with the website - See www.velvettwirlpop.com.au.

Predominantly black, red and grey in colour.

Font used on the website is Honeyscript and Drescher Grotesk Light

Industry/Entity Type

Boutique

Contact Information for Business Card

Velvet Twirl-Pop
Odessa Marlowe - Director
0413 572 064
odessa@velvettwirlpop.com.au

Requirements
Should not have
• No lace, nothing to girly.

```html
<!DOCTYPE html>
<html lang="en">
<head>
<meta charset="utf-8">
<title>Velvet Twirl-Pop — Business Card</title>
<link href="https://fonts.googleapis.com/css2?family=Marcellus&family=Questrial&display=swap" rel="stylesheet">
<style>
  :root {
    --stage: #2a2a2a;
    --card-dark: #0d0d0d;
    --pattern-dark-a: #161616;
    --pattern-dark-b: #0a0a0a;
    --card-light: #dcdad9;
    --pattern-light-a: #e4e2e1;
    --pattern-light-b: #cfcdcc;
    --brand-red: #a3291c;
    --ink: #1a1a1a;
  }
  * { margin: 0; padding: 0; box-sizing: border-box; }
  html, body {
    width: 1200px;
    height: 900px;
    overflow: hidden;
    background: var(--stage);
  }
  .canvas {
    position: relative;
    width: 1200px;
    height: 900px;
  }
  .card {
    position: absolute;
    width: 525px;
    height: 300px;
    overflow: hidden;
    box-shadow: 0 14px 30px rgba(0,0,0,0.55);
  }
  .card-pattern {
    position: absolute;
    inset: 0;
  }

  /* Contact side */
  .card-contact {
    left: 80px;
    top: 130px;
    background: var(--card-light);
  }
  .card-contact .card-pattern {
    background: radial-gradient(ellipse at 35% 55%, var(--pattern-light-b), var(--pattern-light-a) 70%);
  }
  .contact-block {
    position: absolute;
    right: 36px;
    top: 44px;
    text-align: right;
    font-family: "Questrial", sans-serif;
    color: var(--ink);
  }
  .contact-brand {
    display: flex;
    justify-content: flex-end;
    align-items: center;
    gap: 8px;
    font-family: "Marcellus", serif;
    font-size: 15px;
    letter-spacing: 2px;
    color: var(--brand-red);
    margin-bottom: 12px;
  }
  .brand-dot {
    width: 10px;
    height: 10px;
    border-radius: 50%;
    background: var(--brand-red);
  }
  .contact-name {
    font-size: 17px;
    font-weight: 700;
    letter-spacing: 0.5px;
    text-transform: uppercase;
  }
  .contact-role,
  .contact-company,
  .contact-phone {
    font-size: 13px;
    line-height: 1.35;
  }
  .contact-role { margin-bottom: 4px; }
  .contact-company { text-transform: uppercase; }
  .contact-email {
    font-size: 13px;
    margin-top: 12px;
  }

  /* Brand side */
  .card-brand {
    left: 595px;
    top: 470px;
    background: var(--card-dark);
  }
  .card-brand .card-pattern {
    background: radial-gradient(ellipse at 45% 45%, var(--pattern-dark-a), var(--pattern-dark-b) 75%);
  }
  .brand-lockup {
    position: absolute;
    left: 0;
    right: 0;
    top: 118px;
    display: flex;
    justify-content: center;
    align-items: center;
    gap: 14px;
    font-family: "Marcellus", serif;
    font-size: 36px;
    letter-spacing: 6px;
    color: var(--brand-red);
    text-transform: uppercase;
  }
  .brand-lockup .brand-dot {
    width: 14px;
    height: 14px;
  }
  .brand-rule {
    position: absolute;
    left: 0;
    top: 0;
  }
  .brand-web {
    position: absolute;
    left: 0;
    right: 0;
    top: 198px;
    text-align: center;
    font-family: "Questrial", sans-serif;
    font-size: 15px;
    letter-spacing: 1.5px;
    color: var(--brand-red);
  }
</style>
</head>
<body>
<main class="canvas">

  <section class="card card-contact">
    <div class="card-pattern" role="img" aria-label="Soft grey tone-on-tone damask pattern background"></div>
    <div class="contact-block">
      <div class="contact-brand"><span class="brand-dot"></span>Velvet Twirl-Pop</div>
      <p class="contact-name">Odessa Marlowe</p>
      <p class="contact-role">Director</p>
      <p class="contact-company">Velvet Twirl-Pop</p>
      <p class="contact-phone">0413 572 064</p>
      <p class="contact-email">odessa@velvettwirlpop.com.au</p>
    </div>
  </section>

  <section class="card card-brand">
    <div class="card-pattern" role="img" aria-label="Black tone-on-tone damask pattern background"></div>
    <div class="brand-lockup"><span class="brand-dot"></span>Velvet Twirl-Pop</div>
    <svg class="brand-rule" width="525" height="300" viewBox="0 0 525 300" aria-hidden="true">
      <line x1="150" y1="184" x2="490" y2="184" stroke="#a3291c" stroke-width="1"/>
      <line x1="35" y1="232" x2="380" y2="232" stroke="#a3291c" stroke-width="1"/>
    </svg>
    <p class="brand-web">www.velvettwirlpop.com.au</p>
  </section>

</main>
</body>
</html>
```